R.Wren Customer Retention Business Infographic

I am looking to create an infographic by transforming the following data to be used on my website and proposals. I have specific colors that I would like to blend with and a concept of what it could look like, but open. I want to be able to show the comparison...of the two data points side by side.

Target Market(s)

Passionate Business owners

Industry/Entity Type

Business consulting

Font styles to use
Sans Serif

Requirements
Must have
• Concise infographic side by side comparision to use on website and proposals

```html
<!DOCTYPE html>
<html lang="en">
<head>
<meta charset="utf-8">
<title>Customer Retention Infographic</title>
<link href="https://fonts.googleapis.com/css2?family=Poppins:wght@800&family=Baloo+2:wght@700;800&family=Red+Hat+Display:wght@400;800&display=swap" rel="stylesheet">
<style>
  :root {
    --navy: #1b2a5e;
    --navy-deep: #131f4a;
    --ink: #1b2a5c;
    --yellow: #fdd251;
    --orange-soft: #fdbd6e;
    --orange: #f5a83f;
    --grey-panel: #ececec;
    --white: #ffffff;
    --slate: #55709d;
    --backdrop: #e9e9ec;
  }
  * { margin: 0; padding: 0; box-sizing: border-box; }
  html, body { width: 1200px; height: 900px; overflow: hidden; }
  body { background: var(--backdrop); position: relative; }

  .infographic {
    position: absolute; left: 20px; top: 40px;
    width: 1160px; height: 820px; overflow: hidden;
    background: var(--white);
    box-shadow: 0 6px 24px rgba(0,0,0,.18);
  }

  /* Header */
  .header { position: absolute; left: 0; top: 0; width: 1160px; height: 233px;
    background: linear-gradient(180deg, #1e3068 0%, var(--navy) 100%); overflow: hidden; }
  .header-shade { position: absolute; inset: 0; }
  .headline { position: absolute; left: 0; top: 48px; width: 100%; text-align: center;
    font-family: "Poppins", sans-serif; font-weight: 800; line-height: 72px; letter-spacing: -1px; }
  .headline-top { display: block; color: var(--white); font-size: 70px; }
  .headline-bottom { display: block; color: var(--yellow); font-size: 70px; }

  /* Intro band */
  .band { position: absolute; top: 233px; height: 177px; }
  .band-happy { left: 0; width: 579px; background: linear-gradient(90deg, #fdc476 0%, var(--orange-soft) 100%); }
  .band-unhappy { left: 579px; width: 581px; background: var(--yellow); }
  .band-text { position: absolute; font-family: "Baloo 2", sans-serif; font-weight: 700;
    font-size: 22.5px; line-height: 26.5px; color: var(--navy); white-space: nowrap; }
  .band-happy .band-text { left: 195px; top: 36px; }
  .band-unhappy .band-text { left: 233px; top: 40px; }

  .icon-badge { position: absolute; }
  .badge-happy { left: 29px; top: 250px; }
  .badge-unhappy { left: 638px; top: 246px; }

  .vs-badge { position: absolute; left: 546px; top: 293px; width: 64px; height: 64px; border-radius: 50%;
    background: var(--orange); box-shadow: 0 0 0 5px rgba(253,200,90,.7);
    color: var(--white); font-family: "Baloo 2", sans-serif; font-weight: 800; font-size: 26px;
    display: flex; align-items: center; justify-content: center; }

  /* Body */
  .panel-grey { position: absolute; left: 0; top: 410px; width: 1160px; height: 410px; }
  .facts { position: absolute; list-style: none; font-family: "Red Hat Display", sans-serif;
    font-size: 23.3px; line-height: 26.5px; color: var(--ink); white-space: nowrap; }
  .facts li { position: relative; padding-left: 45px; margin-bottom: 26px; }
  .facts b { font-weight: 800; }
  .facts .tick { position: absolute; left: 0; top: 2px; width: 24px; height: 24px; }
  .facts-happy { left: 46px; top: 459px; }
  .facts-unhappy { left: 626px; top: 460px; }

  .footer-link { position: absolute; left: 612px; top: 737px; display: flex; align-items: center; gap: 19px;
    font-family: "Baloo 2", sans-serif; font-weight: 700; font-size: 35px; color: var(--white); }
  .globe { width: 45px; height: 45px; }
</style>
</head>
<body>
<main class="infographic">
  <header class="header">
    <svg class="header-shade" viewBox="0 0 1160 233" preserveAspectRatio="none" aria-hidden="true">
      <polygon points="60,135 1020,100 1160,213 1160,233 110,233" fill="#121c44" opacity=".55"/>
    </svg>
    <h1 class="headline">
      <span class="headline-top">WHEN CUSTOMERS</span>
      <span class="headline-bottom">ENGAGE BUSINESSES FLOURISH</span>
    </h1>
  </header>

  <section class="band band-happy">
    <p class="band-text">When your customers are happy<br>and your business becomes an<br>essential part of their lives...<br>you experience</p>
  </section>
  <section class="band band-unhappy">
    <p class="band-text">When your customers are not<br>ecstatic, you are stuck with<br>stagnant growth and dropping<br>retention rate ...it costs you</p>
  </section>

  <svg class="icon-badge badge-happy" width="148" height="148" viewBox="0 0 148 148" aria-hidden="true">
    <circle cx="74" cy="74" r="72" fill="#fdd27a" opacity=".6"/>
    <circle cx="74" cy="74" r="56" fill="#f2ee8a"/>
    <g fill="#1b2a5e">
      <polygon points="74,40 77,48 85,48 79,53 81,61 74,56 67,61 69,53 63,48 71,48"/>
      <polygon points="53,53 55.5,59 62,59 57,63 59,69 53,65.5 47,69 49,63 44,59 50.5,59"/>
      <polygon points="95,53 97.5,59 104,59 99,63 101,69 95,65.5 89,69 91,63 86,59 92.5,59"/>
      <circle cx="74" cy="76" r="8"/>
      <path d="M60,106 q0,-20 14,-20 q14,0 14,20 z"/>
      <circle cx="54" cy="82" r="6.5"/>
      <path d="M42,106 q0,-17 12,-17 q8,0 9,6 q-5,5 -5,11 z"/>
      <circle cx="94" cy="82" r="6.5"/>
      <path d="M106,106 q0,-17 -12,-17 q-8,0 -9,6 q5,5 5,11 z"/>
    </g>
  </svg>

  <div class="vs-badge">VS</div>

  <svg class="icon-badge badge-unhappy" width="152" height="152" viewBox="0 0 152 152" aria-hidden="true">
    <circle cx="76" cy="76" r="75" fill="#a89a62" opacity=".75"/>
    <circle cx="76" cy="76" r="57" fill="#1b2a5e"/>
    <g fill="#ffffff">
      <rect x="48" y="66" width="11" height="30"/>
      <rect x="63" y="70" width="11" height="26"/>
      <rect x="78" y="76" width="11" height="20"/>
      <rect x="93" y="86" width="11" height="10"/>
    </g>
    <polyline points="44,58 64,54 82,72 96,72" fill="none" stroke="#ffffff" stroke-width="5"/>
    <polygon points="94,62 108,78 90,82" fill="#ffffff"/>
  </svg>

  <svg class="panel-grey" viewBox="0 0 1160 410" preserveAspectRatio="none" aria-hidden="true">
    <defs>
      <linearGradient id="greyFade" x1="0" y1="0" x2="0" y2="1">
        <stop offset="0" stop-color="#ececec"/><stop offset="1" stop-color="#e6e6e6"/>
      </linearGradient>
    </defs>
    <polygon points="0,0 579,0 579,301 555,389 0,389" fill="url(#greyFade)"/>
    <polygon points="579,301 1160,301 1160,410 0,410 0,389 555,389" fill="#55709d"/>
  </svg>

  <ul class="facts facts-happy">
    <li><svg class="tick" viewBox="0 0 24 24"><path d="M21 8 A10 10 0 1 0 21.5 12" fill="none" stroke="#1b2a5c" stroke-width="2.2"/><path d="M7 12l4 4 10-10" fill="none" stroke="#1b2a5c" stroke-width="2.4"/></svg>Boost profits by <b>25%</b> to <b>95%</b> with <b>5%</b><br>increase in customer retention</li>
    <li><svg class="tick" viewBox="0 0 24 24"><path d="M21 8 A10 10 0 1 0 21.5 12" fill="none" stroke="#1b2a5c" stroke-width="2.2"/><path d="M7 12l4 4 10-10" fill="none" stroke="#1b2a5c" stroke-width="2.4"/></svg><b>65%</b> of your business comes from repeat<br>customers.</li>
    <li><svg class="tick" viewBox="0 0 24 24"><path d="M21 8 A10 10 0 1 0 21.5 12" fill="none" stroke="#1b2a5c" stroke-width="2.2"/><path d="M7 12l4 4 10-10" fill="none" stroke="#1b2a5c" stroke-width="2.4"/></svg><b>60%</b> of loyal customers will talk about<br>YOU with their friends and family.</li>
    <li><svg class="tick" viewBox="0 0 24 24"><path d="M21 8 A10 10 0 1 0 21.5 12" fill="none" stroke="#1b2a5c" stroke-width="2.2"/><path d="M7 12l4 4 10-10" fill="none" stroke="#1b2a5c" stroke-width="2.4"/></svg><b>60-70%</b> probability of selling to an<br>existing customer</li>
  </ul>

  <ul class="facts facts-unhappy">
    <li><svg class="tick" viewBox="0 0 24 24"><path d="M21 8 A10 10 0 1 0 21.5 12" fill="none" stroke="#1b2a5c" stroke-width="2.2"/><path d="M7 12l4 4 10-10" fill="none" stroke="#1b2a5c" stroke-width="2.4"/></svg><b>5x</b> higher cost to acquire new customers<br>than retain existing ones</li>
    <li><svg class="tick" viewBox="0 0 24 24"><path d="M21 8 A10 10 0 1 0 21.5 12" fill="none" stroke="#1b2a5c" stroke-width="2.2"/><path d="M7 12l4 4 10-10" fill="none" stroke="#1b2a5c" stroke-width="2.4"/></svg>Costs <b>16 times</b> more to build a long-term<br>relationship with a new customer.</li>
    <li><svg class="tick" viewBox="0 0 24 24"><path d="M21 8 A10 10 0 1 0 21.5 12" fill="none" stroke="#1b2a5c" stroke-width="2.2"/><path d="M7 12l4 4 10-10" fill="none" stroke="#1b2a5c" stroke-width="2.4"/></svg><b>5%</b> to <b>20%</b> probability of selling to a new<br>prospect</li>
  </ul>

  <div class="footer-link">
    <svg class="globe" viewBox="0 0 44 44" aria-hidden="true">
      <circle cx="22" cy="22" r="21" fill="#ffffff"/>
      <g fill="none" stroke="#1b2a5e" stroke-width="2">
        <circle cx="22" cy="22" r="11"/>
        <ellipse cx="22" cy="22" rx="5" ry="11"/>
        <line x1="11" y1="22" x2="33" y2="22"/>
        <line x1="22" y1="11" x2="22" y2="33"/>
      </g>
    </svg>
    <span>www.websiteaddress.com</span>
  </div>
</main>
</body>
</html>
```